Business card for a vending machine business

I need a business card for my vending machine business. The name is Brightwell Snacks, LLC. The card is one-sided, and landscape format. Not portrait.

The information for the card is as follows:

Dora Quinlan
Owner
(555) 314-2096
Brightwellsnacks.example
Info@brightwellsnacks.example

I'd like colors and design elements to match what's in my logo and company name. I'd like to have the checkered flag or racing stripe if possible You can use a border if youd like. You can use a background color if it looks nice and doesn't clash with the logo
Use your creativity. But a white background is perfectly fine. The card can be as simple, yet gets the point across to match the company name and logo.

I uploaded a copy of my logo. I also uploaded a businesses card I started to create, but since it was missing something, I gave up. Another upload has a red thunderbolt and the checkerer flag. Those two uploads are for inspiration. Again, please make sure to make the card landscape, not portrait. Thank you, designers. Good luck to all.

```html
<!DOCTYPE html>
<html lang="en">
<head>
<meta charset="utf-8">
<title>Brightwell Snacks – Business Card</title>
<link rel="stylesheet" href="https://fonts.googleapis.com/css2?family=Lato:wght@400;700&family=Tinos&display=swap">
<style>
  :root {
    --page-bg: #1c1c1c;
    --card-left: #e1a478;
    --card-right: #edd4ac;
    --brand-red: #ee1b1b;
    --ink: #1d1a17;
    --checker: #0d0d0d;
    --divider: #4a3a2c;
  }
  * { margin: 0; padding: 0; box-sizing: border-box; }
  html, body {
    width: 1200px;
    height: 1059px;
    overflow: hidden;
    background: var(--page-bg);
  }
  .card {
    position: absolute;
    left: 179px;
    top: 289px;
    width: 841px;
    height: 480px;
    border-radius: 26px;
    overflow: hidden;
    background: linear-gradient(90deg, var(--card-left) 0%, var(--card-right) 100%);
    font-family: "Lato", sans-serif;
    color: var(--ink);
  }
  .checker-corner {
    position: absolute;
    width: 150px;
    height: 105px;
    background: var(--checker);
    opacity: 0.55;
  }
  .checker-corner.top-left { left: 0; top: 0; clip-path: polygon(0 0, 100% 0, 100% 20%, 45% 100%, 15% 100%, 0 70%); }
  .checker-corner.top-right { right: 0; top: 0; clip-path: polygon(0 0, 100% 0, 100% 70%, 85% 100%, 55% 100%, 0 20%); }
  .checker-corner.bottom-left { left: 0; bottom: 0; clip-path: polygon(0 100%, 100% 100%, 100% 80%, 45% 0, 15% 0, 0 30%); }
  .checker-corner.bottom-right { right: 0; bottom: 0; clip-path: polygon(0 100%, 100% 100%, 100% 30%, 85% 0, 55% 0, 0 80%); }

  .brand {
    position: absolute;
    left: 0;
    right: 0;
    top: 160px;
    display: flex;
    align-items: center;
    justify-content: center;
    gap: 14px;
  }
  .brand-dot {
    width: 30px;
    height: 30px;
    border-radius: 50%;
    background: var(--brand-red);
  }
  .brand-name {
    font-weight: 700;
    font-size: 46px;
    color: var(--brand-red);
    letter-spacing: 0.5px;
  }

  .person {
    position: absolute;
    right: 508px;
    top: 344px;
    text-align: right;
  }
  .person-name {
    font-weight: 700;
    font-size: 35px;
    color: var(--brand-red);
    line-height: 1;
    letter-spacing: -0.3px;
  }
  .person-role {
    font-family: "Tinos", serif;
    font-size: 21px;
    margin-top: 10px;
    line-height: 1;
  }
  .divider {
    position: absolute;
    left: 363px;
    top: 336px;
    width: 2px;
    height: 88px;
    background: var(--divider);
  }
  .contact-list {
    position: absolute;
    left: 385px;
    top: 327px;
    list-style: none;
  }
  .contact-item {
    display: flex;
    align-items: center;
    height: 34px;
    font-size: 22.5px;
  }
  .contact-item svg {
    width: 24px;
    height: 24px;
    margin-right: 11px;
    flex: none;
    fill: var(--brand-red);
  }
</style>
</head>
<body>
  <div class="card">
    <div class="checker-corner top-left" role="img" aria-label="Checkered flag pattern corner"></div>
    <div class="checker-corner top-right" role="img" aria-label="Checkered flag pattern corner"></div>
    <div class="checker-corner bottom-left" role="img" aria-label="Checkered flag pattern corner"></div>
    <div class="checker-corner bottom-right" role="img" aria-label="Checkered flag pattern corner"></div>

    <div class="brand">
      <span class="brand-dot"></span>
      <span class="brand-name">Brightwell Snacks</span>
    </div>

    <div class="person">
      <div class="person-name">Dora Quinlan</div>
      <div class="person-role">Owner</div>
    </div>

    <div class="divider"></div>

    <ul class="contact-list">
      <li class="contact-item">
        <svg viewBox="0 0 24 24" aria-hidden="true"><path d="M6.6 10.8a15.1 15.1 0 0 0 6.6 6.6l2.2-2.2a1 1 0 0 1 1-.25 11.4 11.4 0 0 0 3.6.57 1 1 0 0 1 1 1V20a1 1 0 0 1-1 1A17 17 0 0 1 3 4a1 1 0 0 1 1-1h3.5a1 1 0 0 1 1 1c0 1.25.2 2.46.57 3.6a1 1 0 0 1-.25 1z"/></svg>
        (555) 314-2096
      </li>
      <li class="contact-item">
        <svg viewBox="0 0 24 24" aria-hidden="true"><path d="M2 5h20v14H2z M2 6l10 7 10-7" fill="var(--brand-red)"/><path d="M3 6.5l9 6.3 9-6.3" fill="none" stroke="#edc9a0" stroke-width="1.6"/></svg>
        Info@brightwellsnacks.example
      </li>
      <li class="contact-item">
        <svg viewBox="0 0 24 24" aria-hidden="true"><circle cx="12" cy="12" r="10"/><path d="M12 2v20M2 12h20M12 2c-3.5 3-3.5 17 0 20M12 2c3.5 3 3.5 17 0 20" fill="none" stroke="#edc9a0" stroke-width="1.4"/></svg>
        Brightwellsnacks.example
      </li>
    </ul>
  </div>
</body>
</html>
```